cartNest - a stylish trolley for apartments

We neede a simple website to sell our Trolley, for apartment use.
The colour theme is red, blask & white. Our logo is attached and this needs to be on the Home page.
The website only needs a Home Page plus 4 other pges.
In the attachment you will find a site map.

You can check out the following two sites to see what I like:
www.plinthgallery.example/design-showcase-inspiration/minimalist-portfolio-website/
www.brightquarry.example/inspiration/40-beautiful-web-design-portfolios/ in this site especially
Dario Menezes
K B Forge
Nine 17 Studio
Oliver Marsh

And especially Lamp - I ike the simpicity of the site esp as we are only selling one product

Target Market(s)

Apartment dwellers

Industry/Entity Type

Apartment

Requirements
Must have
• This website must have 4 pages.
We need Corvo, Ledgerline and Quidly portals.
Order Form for Trolley
Payment form.

```html
<!DOCTYPE html>
<html lang="en">
<head>
<meta charset="utf-8">
<title>cartNest – a stylish trolley for apartments</title>
<link href="https://fonts.googleapis.com/css2?family=Questrial&family=Arimo:ital,wght@0,400;0,700;1,700&family=Tinos:ital@0;1&display=swap" rel="stylesheet">
<style>
:root{
  --red:#c8173a;
  --red-dark:#a50f2c;
  --bg:#1f1f1f;
  --bg-deep:#141414;
  --text:#e6e6e6;
  --muted:#8a8a8a;
  --white:#ffffff;
  --field:#e2e2e2;
}
*{box-sizing:border-box;margin:0;padding:0}
html,body{width:700px;height:1200px;overflow:hidden}
body{position:relative;background:linear-gradient(#262626 0,#1d1d1d 380px,#1a1a1a 1000px);font-family:"Arimo",Arial,sans-serif;color:var(--text)}
.abs{position:absolute}
.band{position:absolute;left:0;width:700px;height:40px;background:radial-gradient(ellipse 55% 100% at 50% 0,rgba(0,0,0,.55),rgba(0,0,0,0))}
.brand{left:88px;top:88px;font-family:"Questrial",sans-serif;font-size:34px;color:var(--white);letter-spacing:-1px}
.brand-mark{left:88px;top:30px;width:40px;height:40px;background:var(--red)}
.account{right:96px;top:10px;font-size:6.5px;font-weight:700;color:var(--white)}
.account .hl{color:var(--red)}
.account .dim{color:var(--muted);font-weight:400}
.currency{left:388px;top:29px;font-size:6.5px;font-weight:700;color:#ccc;display:flex;align-items:center;gap:3px}
.currency span.box{display:inline-block;width:8px;height:11px;background:var(--white);color:#222;text-align:center;line-height:11px;font-size:7px}
.currency span.box.on{background:var(--red);color:var(--white)}
.search{left:465px;top:24px;width:111px;height:18px;background:var(--white);border-radius:4px}
.btn{background:var(--red);color:var(--white);font-weight:700;border-radius:3px;text-align:center;box-shadow:inset 0 -2px 0 var(--red-dark)}
.go{left:580px;top:24px;width:24px;height:18px;font-size:8px;line-height:18px}
.nav{left:319px;top:106px;display:flex;gap:0;font-family:"Questrial",sans-serif;font-weight:700;font-size:9.5px;color:var(--white)}
.nav a{color:inherit;text-decoration:none;padding:0 7px;height:19px;line-height:19px;margin-right:7px;-webkit-text-stroke:.25px currentColor}
.nav a.current{background:var(--red);border-radius:3px}
.rule{left:88px;top:136px;width:524px;border-top:1px dashed #555}
.hero-title{left:89px;top:174px;font-family:"Arimo",sans-serif;font-style:italic;font-weight:700;color:var(--white);line-height:1.15}
.hero-title .small{font-size:18px;display:block}
.hero-title .big{font-size:27px;display:block;margin-top:2px}
.hero-copy{left:91px;top:277px;width:175px;font-size:7.6px;line-height:13px;color:#ddd}
.dots{left:205px;top:340px;display:flex;gap:4px}
.dots i{width:9px;height:9px;border-radius:50%;background:#555}
.dots i.on{background:var(--red)}
.frame{border:3px solid var(--white);background:var(--white)}
.hero-img{left:271px;top:147px;width:339px;height:226px}
.ph{width:100%;height:100%}
.h2{font-family:"Arimo",sans-serif;font-style:italic;font-weight:700;font-size:14px;color:var(--red)}
.about-img{left:93px;top:457px;width:87px;height:129px}
.about-copy{left:194px;top:456px;width:416px;font-size:7.4px;line-height:13.1px;color:#ddd}
.about-copy p+p{margin-top:13px}
.about-copy ul{list-style:none}
.about-copy li::before{content:"•";display:inline-block;width:20px}
.card{width:164px;text-align:center}
.card .frame{height:101px}
.card h3{font-family:"Tinos",serif;font-style:italic;font-weight:400;font-size:11.5px;color:#666;margin-top:10px}
.card .date{font-size:6.3px;color:var(--red);margin-top:4px}
.card p{font-size:7.2px;line-height:10px;color:#aaa;margin:8px 12px 0}
.card .more{display:inline-block;width:46px;height:19px;line-height:19px;font-size:7.4px;font-weight:400}
.quote{left:93px;top:936px;width:514px;height:46px;background:var(--white)}
.quote blockquote{position:absolute;left:15px;top:7px;width:400px;font-family:"Tinos",serif;font-style:italic;font-size:7.6px;line-height:12px;color:#333}
.quote cite{position:absolute;left:388px;top:32px;font-family:"Tinos",serif;font-style:italic;font-size:7.6px;color:var(--red)}
.quote .more{position:absolute;left:444px;top:13px;width:47px;height:20px;line-height:20px;font-size:6.4px}
.footer{left:0;top:1000px;width:700px;height:200px;background:var(--bg-deep);border-top:3px solid var(--red)}
.fcol{top:1025px}
.fcol h4{font-family:"Questrial",sans-serif;font-size:10px;color:var(--white);-webkit-text-stroke:.2px #fff;margin-bottom:18px}
.fcol ul{list-style:none;font-size:6.6px;font-weight:700;color:#bbb}
.fcol li{height:13.2px;display:flex;align-items:center}
.fcol li::before{content:"";width:4px;height:4px;border-radius:50%;background:var(--white);margin-right:7px}
.social li{height:26px}
.social .icon{width:18px;height:18px;border-radius:50%;background:#2f6fa8;border:2px solid #cfe0ef;margin-right:7px;margin-left:1px}
.field{width:108px;height:18px;background:var(--field);border-radius:2px;font-size:6.5px;font-style:italic;color:#999;padding-left:5px;line-height:18px;margin-bottom:3px}
.submit{margin-left:62px;margin-top:4px;width:46px;height:20px;line-height:20px;font-size:7px}
.pay{left:301px;top:1150px;display:flex;gap:3px}
.pay span{width:26px;height:17px;background:var(--white);border-radius:2px;color:#234;font-size:5.6px;font-weight:700;text-align:center;line-height:17px}
.legal{left:0;top:1179px;width:700px;text-align:center;font-size:6.2px;color:#888}
</style>
</head>
<body>

<header>
  <div class="abs brand-mark"></div>
  <div class="abs brand">cartNest</div>

  <div class="abs account"><span class="hl">Login</span> &nbsp;•&nbsp; Sign Up &nbsp;&nbsp;&nbsp;&nbsp; <span class="dim">Shopping Cart &nbsp;|&nbsp; 0 item(s) - </span><span class="hl">$ 0.00</span></div>
  <div class="abs currency">Currency&nbsp; <span class="box on">€</span><span class="box">£</span><span class="box">$</span></div>
  <div class="abs search">
    <svg width="12" height="18" viewBox="0 0 12 18"><circle cx="7" cy="8" r="3" fill="none" stroke="#aaa" stroke-width="1.2"/><line x1="9.2" y1="10.2" x2="11" y2="12" stroke="#aaa" stroke-width="1.2"/></svg>
  </div>
  <div class="abs btn go">Go</div>

  <nav class="abs nav">
    <a class="current">Home</a><a>cartNest</a><a>Gallery</a><a>Shopping Cart</a><a>Contact Us</a>
  </nav>
  <div class="abs rule"></div>
</header>

<section class="hero">
  <h1 class="abs hero-title"><span class="small">Originated from</span><span class="big">our personal</span><span class="big">experience</span></h1>
  <p class="abs hero-copy">From our personal experience of apartment living, and the hassle of taking shopping, luggage, etc, from your car to your apartment.</p>
  <div class="abs dots"><i class="on"></i><i></i><i></i><i></i></div>
  <div class="abs frame hero-img">
    <div class="ph" role="img" aria-label="Brass luggage trolley with red suitcases in an apartment entrance hall" style="background:linear-gradient(90deg,#c9b9a6 0,#8a6a4c 35%,#3a3a44 55%,#b89a7a 75%,#d8d4cc 100%)"></div>
    <svg class="abs" style="left:4px;top:96px" width="22" height="30" viewBox="0 0 22 30"><path d="M20 2 L4 15 L20 28 Z" fill="rgba(0,0,0,.45)"/></svg>
    <svg class="abs" style="right:4px;top:96px" width="22" height="30" viewBox="0 0 22 30"><path d="M2 2 L18 15 L2 28 Z" fill="rgba(0,0,0,.45)"/></svg>
  </div>
</section>

<div class="band" style="top:398px"></div>

<section class="about">
  <h2 class="abs h2" style="left:93px;top:424px">About cartNest</h2>
  <div class="abs frame about-img"><div class="ph" role="img" aria-label="Owner standing beside a chrome trolley in a hallway" style="background:linear-gradient(#4a4a4a,#6a5a4a 70%,#8a5a38)"></div></div>
  <div class="abs about-copy">
    <p>cartNest originated from our personal experience of apartment living, and the hassle of taking shopping, luggage, etc, from your car to your apartment. We have sourced trolleys from all over the place, and failed to find a versatile, strong trolley, which also looked stylish. Our emphasis is on &nbsp;style because we wanted a trolley which would sit inside our front door, and look great! We are busy people and wanted a trolley, at hand.! &nbsp;We were tired of trolleys which had to be packed up and put in cupboards. This action continuously weakened the trolleys and parts broke easily due to the" wear and tear".</p>
    <p>Most domestic trolleys are not strong, and nearly always &nbsp;look like they belong in a factory or workshop. &nbsp;We decided that we wanted a trolley that:</p>
    <ul>
      <li>Looked attractive living anywhere in our apartment, and not inside a cupboard</li>
      <li>Offered both hanging and flat-bed options.</li>
    </ul>
  </div>
</section>

<div class="band" style="top:606px"></div>

<section class="products">
  <h2 class="abs h2" style="left:93px;top:634px">Our cartNest</h2>

  <article class="abs card" style="left:93px;top:663px">
    <div class="frame"><div class="ph" role="img" aria-label="Close-up of trolley wheels and base" style="background:linear-gradient(#cfc7bb,#4a3a36 55%,#9a6a4a)"></div></div>
    <h3>cartNest Everywhere</h3>
    <div class="date">Posted July 13th, 2012</div>
    <p>Looked attractive living anywhere in our apartment, and not inside a cupboard...</p>
    <div class="btn more" style="margin-top:8px">Read more</div>
  </article>

  <article class="abs card" style="left:268px;top:663px">
    <div class="frame"><div class="ph" role="img" aria-label="Chrome hanging rail of the trolley" style="background:linear-gradient(#b8c2cc,#9aa6b2)"></div></div>
    <h3>cartNest Everywhere</h3>
    <div class="date">Posted July 13th, 2012</div>
    <p>cartNest originated from our personal experience of apartment living, and the hassle of taking shopping, luggage, etc</p>
    <div class="btn more" style="margin-top:9px">Read more</div>
  </article>

  <article class="abs card" style="left:443px;top:663px">
    <div class="frame"><div class="ph" role="img" aria-label="Trolley loaded with bags against a teal wall" style="background:linear-gradient(#2a4a58,#3a4a52 60%,#8a4a3a)"></div></div>
    <h3>cartNest Everywhere</h3>
    <div class="date">Posted July 13th, 2012</div>
    <p>We are busy people and wanted a trolley, at hand.!</p>
    <div class="btn more" style="margin-top:9px">Read more</div>
  </article>
</section>

<div class="band" style="top:878px"></div>

<section class="testimonial">
  <h2 class="abs h2" style="left:92px;top:904px">What They Say?</h2>
  <div class="abs quote">
    <blockquote>“Duis autem vel eum iriure dolor in hendrerit in vulputate velit esse molestie consequat, vel illum dolore eu feugiat nulla facilisis at vero eros et accumsan et iusto odio dignissim qui blandit praesent luptatum zzril delenit”</blockquote>
    <cite>- John Doe -</cite>
    <div class="btn more">Read more</div>
  </div>
</section>

<footer>
  <div class="abs footer"></div>

  <div class="abs fcol" style="left:112px">
    <h4>Site map</h4>
    <ul><li>Home</li><li>cartNest</li><li>Why choose cartNest</li><li>How to make cartNest</li><li>Gallery</li><li>Contact Us</li></ul>
  </div>
  <div class="abs fcol" style="left:241px">
    <h4>Our Services Area</h4>
    <ul><li>Hotels</li><li>Apartments</li><li>Restaurant</li><li>Hospitals</li></ul>
  </div>
  <div class="abs fcol" style="left:374px">
    <h4>Find Us</h4>
    <ul class="social" style="margin-top:-5px"><li><span class="icon"></span>Linkwall</li><li><span class="icon" style="background:#3aa0d8"></span>Chirpline</li></ul>
  </div>
  <div class="abs fcol" style="left:485px">
    <h4 style="margin-bottom:14px">Newsletter</h4>
    <div class="field">Your name</div>
    <div class="field">Your email</div>
    <div class="btn submit">SUBMIT</div>
  </div>

  <div class="abs pay"><span>Corvo</span><span>Ledgerline</span><span>Quidly</span></div>
  <div class="abs legal">Help &nbsp;|&nbsp; Terms &amp; Condition &nbsp;|&nbsp; Privacy Policy &nbsp;-&nbsp; Copyright © 2012 - cartNest &nbsp;|&nbsp; All Right Reserved</div>
</footer>

</body>
</html>
```